New cool to-go cup for KELMO Coffee

UPDATE MARCH 18: Please read the attached document "Design ideas - Front" with a mock-up of the design we are looking for. And please don't change the logo.

We are looking for a new cool design for our to-go cups in kraft paper (same style as the attached photo).

The idea:

We have three different cups sizes: 6oz, 8oz and 12oz. We call them “Tiny-Lark” (6oz), “Mid-Wren” (8oz) and “Tall-heron” (12oz) (refers to the size in milliliters). We would like to include this in the cup design. Please see the attached sketch of the idea ("Design ideas - Front").

The backside of the cup should have the attached text and logo ("Design ideas - Back").

But other ideas are also very welcome too! Maybe just a simple cup with the logo.

Please keep the design very minimalistic. The more simple the better.

Target Market(s)

Young urban people

Industry/Entity Type

Coffee shop

Font styles to use
Sans Serif

Requirements
Must have
• Kraft paper cups

```html
<!DOCTYPE html>
<html lang="en">
<head>
<meta charset="utf-8">
<title>KELMO Coffee – To-go Cup Wraps</title>
<link rel="stylesheet" href="https://fonts.googleapis.com/css2?family=Montserrat:wght@400;500;700&display=swap">
<style>
  :root {
    --bg: #f3f4f6;
    --kraft-light: #ddb487;
    --kraft-mid: #d0a474;
    --kraft-dark: #9a6c3c;
    --ink: #3a2214;
  }
  * { box-sizing: border-box; margin: 0; padding: 0; }
  html, body { width: 1200px; height: 1000px; overflow: hidden; }
  body {
    position: relative;
    background: var(--bg);
    font-family: "Montserrat", sans-serif;
    color: var(--ink);
  }
  .wrap {
    position: absolute;
    display: flex;
    flex-direction: column;
    align-items: center;
    text-align: center;
    background: linear-gradient(90deg, var(--kraft-mid) 0%, var(--kraft-light) 22%, var(--kraft-mid) 60%, var(--kraft-dark) 100%);
    border-radius: 2px;
  }
  .wrap--tiny { font-size: 10px; width: 190px; height: 220px; top: 180px; }
  .wrap--mid  { font-size: 12px; width: 215px; height: 265px; top: 140px; }
  .wrap--tall { font-size: 15px; width: 260px; height: 320px; top: 585px; }

  .wrap--front { justify-content: center; padding-bottom: 1em; }
  .wrap--back  { padding-top: 3.4em; }

  .brand {
    display: flex;
    align-items: center;
    gap: 0.45em;
    font-weight: 700;
    font-size: 1em;
    letter-spacing: 0.04em;
    color: var(--ink);
  }
  .brand__dot {
    width: 1.1em; height: 1.1em;
    border-radius: 50%;
    background: var(--ink);
  }
  .wrap--back .brand { font-size: 1.2em; }

  .size-tag { margin-top: 0.7em; font-size: 1.75em; font-weight: 400; letter-spacing: 0.01em; }
  .size-tag b { font-weight: 700; }

  .story { margin-top: 2em; font-size: 0.85em; line-height: 1.3; font-weight: 400; }
  .site  { margin-top: 1.6em; font-size: 0.85em; font-weight: 700; }
  .handle { margin-top: 1.3em; font-size: 0.85em; }
</style>
</head>
<body>
  <!-- Tiny-Lark -->
  <section class="wrap wrap--tiny wrap--front" style="left:120px">
    <div class="brand"><span class="brand__dot"></span>KELMO Coffee</div>
    <p class="size-tag">#<b>tiny</b>lark</p>
  </section>
  <section class="wrap wrap--tiny wrap--back" style="left:320px">
    <div class="brand"><span class="brand__dot"></span>KELMO Coffee</div>
    <p class="story">Read about your coffee<br>and the dedicated farmers<br>who made this cup possible:</p>
    <p class="site">www.kelmocoffee.com</p>
    <p class="handle">@kelmocoffee</p>
  </section>

  <!-- Mid-Wren -->
  <section class="wrap wrap--mid wrap--front" style="left:645px">
    <div class="brand"><span class="brand__dot"></span>KELMO Coffee</div>
    <p class="size-tag">#<b>mid</b>wren</p>
  </section>
  <section class="wrap wrap--mid wrap--back" style="left:870px">
    <div class="brand"><span class="brand__dot"></span>KELMO Coffee</div>
    <p class="story">Read about your coffee<br>and the dedicated farmers<br>who made this cup possible:</p>
    <p class="site">www.kelmocoffee.com</p>
    <p class="handle">@kelmocoffee</p>
  </section>

  <!-- Tall-heron -->
  <section class="wrap wrap--tall wrap--front" style="left:310px">
    <div class="brand"><span class="brand__dot"></span>KELMO Coffee</div>
    <p class="size-tag">#<b>tall</b>heron</p>
  </section>
  <section class="wrap wrap--tall wrap--back" style="left:585px">
    <div class="brand"><span class="brand__dot"></span>KELMO Coffee</div>
    <p class="story">Read about your coffee<br>and the dedicated farmers<br>who made this cup possible:</p>
    <p class="site">www.kelmocoffee.com</p>
    <p class="handle">@kelmocoffee</p>
  </section>
</body>
</html>
```